Moving comapny Postcard mailer Design

I am looking for a 6x9 postcard with real images of our team. I would like to add the same review we currently have , I want the colors of the postcard to be orange and white. I want the team picture to be enlarged with the other pictures to be mimized. I will add example postcards to give rough ideas. My company is called Brandwell Moving and the postcards with that name are our current postcards. The additional postcards are from other companies who have better postcards than mine. My goal is for my postcard to be better that theirs.

Target Market(s)

Wealthy people in the 35+ age group

Industry/Entity Type

Moving company

Requirements
Must have
• Beauty

```html
<!DOCTYPE html>
<html lang="en">
<head>
<meta charset="utf-8">
<title>Brandwell Moving Postcard</title>
<link href="https://fonts.googleapis.com/css2?family=Montserrat:ital,wght@0,400;0,600;0,700;0,800;1,400;1,500&display=swap" rel="stylesheet">
<style>
  :root {
    --orange: #e4522a;
    --orange-soft: #ee7a45;
    --white: #ffffff;
    --paper: #ffffff;
    --dash: #f39a74;
    --photo-mid: #a08c80;
    --photo-right: #b9bdb3;
  }
  * { margin: 0; padding: 0; box-sizing: border-box; }
  html, body { width: 1200px; height: 821px; overflow: hidden; background: var(--paper); }
  body { font-family: 'Montserrat', sans-serif; }
  .postcard { position: relative; width: 1200px; height: 821px; background: var(--paper); overflow: hidden; }

  .team-photo {
    position: absolute; left: 0; top: 0; width: 1200px; height: 560px;
    background: linear-gradient(90deg, #e8642f 0%, #e8703d 30%, #c07a5c 45%, var(--photo-mid) 60%, var(--photo-right) 100%);
  }
  .photo-band {
    position: absolute; left: 0; top: 543px; width: 1200px; height: 17px;
    background: linear-gradient(90deg, var(--orange) 0%, #e96a3c 60%, #e9794a 100%);
  }

  .headline {
    position: absolute; left: 91px; top: 78px;
    color: var(--white); font-weight: 800; font-size: 88px; line-height: 92px; letter-spacing: -0.5px;
  }
  .tagline {
    position: absolute; left: 91px; top: 270px;
    color: var(--white); font-weight: 400; font-size: 41px; line-height: 50px;
  }
  .brand-mark {
    position: absolute; left: 91px; top: 430px; display: flex; align-items: center; gap: 10px;
    color: var(--white); font-weight: 700; font-size: 19px;
  }
  .brand-mark .dot { width: 22px; height: 22px; border-radius: 50%; background: var(--white); }

  .contact-cta {
    position: absolute; left: 714px; top: 348px;
    color: var(--white); font-style: italic; font-weight: 500; font-size: 37px;
  }
  .cta-arrow { position: absolute; left: 1035px; top: 352px; }
  .contact-box {
    position: absolute; left: 713px; top: 404px; width: 365px; height: 108px;
    background: var(--white); border-radius: 10px; text-align: center; padding-top: 12px;
  }
  .contact-box .phone { color: var(--orange); font-weight: 700; font-size: 40px; line-height: 48px; }
  .contact-box .web { color: var(--orange); font-style: italic; font-size: 24px; line-height: 30px; }

  .coupon {
    position: absolute; top: 599px; width: 203px; height: 149px;
    background: var(--orange); border: 2px dashed var(--dash); border-radius: 3px;
    color: var(--white); text-align: center; padding-top: 10px;
  }
  .coupon .amount { font-weight: 800; font-size: 35px; line-height: 44px; }
  .coupon .amount sup { font-size: 20px; vertical-align: 14px; margin-right: 1px; }
  .coupon .label { font-size: 17px; line-height: 22px; }
  .coupon .limit { font-weight: 700; font-size: 24px; line-height: 30px; }
  .coupon .note { font-style: italic; font-size: 16px; line-height: 24px; }
  .coupon-25 { left: 61px; }
  .coupon-50 { left: 279px; }
  .coupon-100 { left: 500px; }

  .review { position: absolute; left: 731px; top: 588px; width: 405px; }
  .review .stars { display: flex; justify-content: center; gap: 7px; margin-bottom: 8px; }
  .review blockquote {
    color: var(--orange); font-style: italic; font-size: 14.4px; line-height: 17px;
    text-align: justify; text-align-last: center;
  }
</style>
</head>
<body>
<div class="postcard">
  <div class="team-photo" role="img" aria-label="Photo of the moving team in black uniforms standing in front of an open white box truck"></div>
  <div class="photo-band"></div>

  <h1 class="headline">BRANDWELL<br>MOVING</h1>
  <p class="tagline">Let us help you with<br>Heavy Lifting!</p>

  <div class="brand-mark"><span class="dot"></span>Brandwell Moving</div>

  <p class="contact-cta">Contact us now</p>
  <svg class="cta-arrow" width="100" height="95" viewBox="0 0 100 95" fill="none" stroke="#ffffff" stroke-width="3" stroke-linecap="round" stroke-linejoin="round">
    <path d="M2 14 C20 12 35 10 45 14 C55 20 50 38 40 36 C28 33 38 10 60 8 C85 6 98 30 88 52 C82 66 72 76 60 84"/>
    <path d="M60 84 L62 70 M60 84 L73 82"/>
  </svg>
  <div class="contact-box">
    <div class="phone">(865) 555-0142</div>
    <div class="web">www.brandwellmovers.com</div>
  </div>

  <div class="coupon coupon-25">
    <div class="amount"><sup>$</sup>25 OFF</div>
    <div class="label">MOVES UNDER</div>
    <div class="limit">$1000</div>
    <div class="note">With this card</div>
  </div>
  <div class="coupon coupon-50">
    <div class="amount"><sup>$</sup>50 OFF</div>
    <div class="label">MOVES UNDER</div>
    <div class="limit">$1000</div>
    <div class="note">With this card</div>
  </div>
  <div class="coupon coupon-100">
    <div class="amount"><sup>$</sup>100 OFF</div>
    <div class="label">MOVES UNDER</div>
    <div class="limit">$1000</div>
    <div class="note">With this card</div>
  </div>

  <div class="review">
    <div class="stars">
      <svg width="20" height="19" viewBox="0 0 24 23"><path fill="#e4522a" d="M12 0l3.5 7.5 8.2 1-6 5.7 1.6 8.1L12 18.3 4.7 22.3l1.6-8.1-6-5.7 8.2-1z"/></svg>
      <svg width="20" height="19" viewBox="0 0 24 23"><path fill="#e4522a" d="M12 0l3.5 7.5 8.2 1-6 5.7 1.6 8.1L12 18.3 4.7 22.3l1.6-8.1-6-5.7 8.2-1z"/></svg>
      <svg width="20" height="19" viewBox="0 0 24 23"><path fill="#e4522a" d="M12 0l3.5 7.5 8.2 1-6 5.7 1.6 8.1L12 18.3 4.7 22.3l1.6-8.1-6-5.7 8.2-1z"/></svg>
      <svg width="20" height="19" viewBox="0 0 24 23"><path fill="#e4522a" d="M12 0l3.5 7.5 8.2 1-6 5.7 1.6 8.1L12 18.3 4.7 22.3l1.6-8.1-6-5.7 8.2-1z"/></svg>
      <svg width="20" height="19" viewBox="0 0 24 23"><path fill="#e4522a" d="M12 0l3.5 7.5 8.2 1-6 5.7 1.6 8.1L12 18.3 4.7 22.3l1.6-8.1-6-5.7 8.2-1z"/></svg>
    </div>
    <blockquote>“This company is incredible! After working all day, they came to our house and without skipping a beat began efficiently moving our heavy household items. They had a great attitude, very friendly, and clearly enjoyed working with each other! They took extremely good care of my household items. Thank you for a great experience!”</blockquote>
  </div>
</div>
</body>
</html>
```